Road Sign at our office 84 in X 48 in - Small Billboard

Kestrel Electrical
Electrical & Lighting Services

- we need a sign design for our small business/company based in Calhoun, GA called Kestrel Electrical - "our mission is to provide Northwest Georgia with dependable, high-quality electrical services that prioritize safety, integrity, and long-term reliability. As a woman-owned business with over 25 years of experience, we are committed to delivering exceptional workmanship and personalized service for every commercial, residential, and industrial project we undertake. We stand behind our work with a lifetime warranty—because your trust is our most powerful connection."

display logo, phone number, and open to other ideas without being cluttered, maybe instead of full website address, just use @ksrelectrical and it will send them to all of our website and socials...

it needs to be easy to read as they drive down the road
this is a place where people may be traveling at high speeds, make sure it's easy to see and understand at a glance.
It will be hanging 20-24ft from the ground. Like a small billboard.

https://ksrelectricworks.com/

Industry/Entity Type

Electrical Contractor

Requirements
Nice to have
• match the look and feel of website and socials

```html
<!DOCTYPE html>
<html lang="en">
<head>
<meta charset="utf-8">
<title>Kestrel Electrical – Road Sign</title>
<link rel="stylesheet" href="https://fonts.googleapis.com/css2?family=Open+Sans:wght@600;800&family=Oswald:wght@400;500&display=swap">
<style>
  :root {
    --page-bg: #1c1c1c;
    --brand-orange: #e94e1b;
    --brand-amber: #f29a00;
    --check-amber: #f7a21b;
    --ink: #1a1a1a;
    --white: #ffffff;
    --star: #e94e1b;
  }
  * { margin: 0; padding: 0; box-sizing: border-box; }
  html, body {
    width: 987px; height: 1200px; overflow: hidden;
    background: var(--page-bg);
  }
  .canvas { position: relative; width: 987px; height: 1200px; }
  .billboard {
    position: absolute; left: 43px; top: 343px;
    width: 900px; height: 514px;
    background: var(--brand-orange);
    overflow: hidden;
  }
  .billboard-shapes { position: absolute; inset: 0; }
  .headline {
    position: absolute; left: 50px; top: 28px;
    font-family: "Open Sans", sans-serif; font-weight: 800;
    font-size: 80px; line-height: 89px; letter-spacing: 0.5px;
    color: var(--white); text-transform: uppercase; white-space: nowrap;
  }
  .headline-rule {
    position: absolute; left: 53px; top: 219px;
    width: 252px; height: 3px; background: var(--ink);
  }
  .service-list { list-style: none; }
  .service {
    position: absolute;
    display: flex; align-items: center; gap: 10px; height: 56px;
    font-family: "Oswald", sans-serif; font-weight: 400;
    font-size: 50px; line-height: 56px; color: var(--white);
    text-transform: uppercase; letter-spacing: -2px; white-space: nowrap;
  }
  .service--commercial { left: 53px; top: 237px; }
  .service--residential { left: 341px; top: 237px; }
  .service--industrial { left: 53px; top: 304px; }
  .service-tick { width: 42px; height: 42px; flex: none; }
  .credentials {
    position: absolute; left: 40px; top: 406px;
    font-family: "Open Sans", sans-serif; font-weight: 600;
    font-size: 18.5px; line-height: 26px; color: var(--white);
    letter-spacing: 0.3px; white-space: nowrap;
  }
  .credentials .star { color: var(--star); margin: 0 10px; }
  .contact-phone, .contact-handle {
    position: absolute; top: 440px;
    font-family: "Oswald", sans-serif; font-weight: 500;
    font-size: 41px; line-height: 50px; color: var(--ink);
    white-space: nowrap; transform-origin: left center;
  }
  .contact-phone { left: 39px; letter-spacing: -1px; }
  .contact-handle { left: 267px; letter-spacing: -1px; transform: scaleX(0.76); }
  .contact-divider {
    position: absolute; left: 254px; top: 448px;
    width: 2px; height: 36px; background: var(--brand-orange);
  }
  .brand-name {
    position: absolute; left: 600px; top: 388px;
    display: flex; align-items: center; gap: 16px;
    font-family: "Open Sans", sans-serif; font-weight: 800;
    font-size: 42px; line-height: 46px; color: var(--ink);
  }
  .brand-dot {
    width: 40px; height: 40px; border-radius: 50%;
    background: var(--brand-orange); flex: none;
  }
</style>
</head>
<body>
<div class="canvas">
  <section class="billboard" aria-label="Kestrel Electrical road sign">
    <svg class="billboard-shapes" width="900" height="514" viewBox="0 0 900 514" aria-hidden="true">
      <rect class="credentials-band" x="0" y="404" width="520" height="29" fill="#1a1a1a"/>
      <rect class="bottom-edge" x="0" y="505" width="900" height="9" fill="#ffffff"/>
      <path class="contact-band" d="M0 432 H505 L478 490 Q470 505 450 505 H0 Z" fill="#f29a00"/>
      <path class="brand-panel" d="M468 514 L528 372 Q538 348 568 348 H900 V514 Z" fill="#ffffff"/>
    </svg>

    <h1 class="headline">Electrical &amp;<br>Lighting Services</h1>
    <div class="headline-rule"></div>

    <ul class="service-list">
      <li class="service service--commercial">
        <svg class="service-tick" viewBox="0 0 42 42" aria-hidden="true"><rect x="3" y="8" width="31" height="31" rx="5" fill="none" stroke="#f7a21b" stroke-width="4"/><path d="M11 22 L18 30 L38 3" fill="none" stroke="#f7a21b" stroke-width="5" stroke-linecap="round" stroke-linejoin="round"/></svg>
        Commercial
      </li>
      <li class="service service--residential">
        <svg class="service-tick" viewBox="0 0 42 42" aria-hidden="true"><rect x="3" y="8" width="31" height="31" rx="5" fill="none" stroke="#f7a21b" stroke-width="4"/><path d="M11 22 L18 30 L38 3" fill="none" stroke="#f7a21b" stroke-width="5" stroke-linecap="round" stroke-linejoin="round"/></svg>
        Residential
      </li>
      <li class="service service--industrial">
        <svg class="service-tick" viewBox="0 0 42 42" aria-hidden="true"><rect x="3" y="8" width="31" height="31" rx="5" fill="none" stroke="#f7a21b" stroke-width="4"/><path d="M11 22 L18 30 L38 3" fill="none" stroke="#f7a21b" stroke-width="5" stroke-linecap="round" stroke-linejoin="round"/></svg>
        Industrial
      </li>
    </ul>

    <p class="credentials">25+ YEARS EXPERIENCE<span class="star">★</span>LIFETIME WARRANTY</p>
    <p class="contact-phone">706 555 0184</p>
    <span class="contact-divider"></span>
    <p class="contact-handle">@KSRELECTRICAL</p>

    <div class="brand-name">
      <span class="brand-dot"></span>
      <span>Kestrel<br>Electrical</span>
    </div>
  </section>
</div>
</body>
</html>
```